BrambleWare business card

Looking for business card design that supports our company/software values. We have 2 logo designs at the moment but open to change if you think you can enhance the brand. Check out website www.brambleware.com.au.

Target Market(s)

Education

Contact Information for Business Card

Name, title, mobile, email and website

Font styles to use
Sans Serif

Colors

Designer to choose colors to be used in the design.

Requirements
Must have
• BrambleWare logo with tree and tagline on rear side with dark grey background colour

```html
<!DOCTYPE html>
<html lang="en">
<head>
<meta charset="UTF-8">
<title>BrambleWare Business Card</title>
<link href="https://fonts.googleapis.com/css2?family=Raleway:wght@400;500;600;700&display=swap" rel="stylesheet">
<style>
  :root {
    --backdrop: #dcdcdc;
    --card-white: #ffffff;
    --ink-grey: #555555;
    --ink-dark: #444444;
    --rule-grey: #8a8a8a;
    --brand-green: #4f7a20;
    --brand-green-deep: #436a18;
    --accent-yellow: #f8bd3c;
    --reverse-text: #ffffff;
  }
  * { margin: 0; padding: 0; box-sizing: border-box; }
  html, body { width: 1200px; height: 1200px; overflow: hidden; }
  body {
    background: var(--backdrop);
    font-family: "Raleway", Arial, sans-serif;
    position: relative;
  }
  .card {
    position: absolute;
    left: 262px;
    width: 686px;
    height: 392px;
  }
  .card-front { top: 165px; background: var(--card-white); }
  .card-back {
    top: 653px;
    background: linear-gradient(180deg, var(--brand-green) 0%, var(--brand-green-deep) 100%);
  }

  /* front: brand block */
  .brand-mark {
    position: absolute; left: 40px; top: 64px;
    width: 40px; height: 40px; border-radius: 50%;
    background: var(--brand-green);
  }
  .brand-name {
    position: absolute; left: 94px; top: 54px;
    font-size: 36px; font-weight: 500; color: var(--ink-grey);
    letter-spacing: 0.2px;
  }
  .brand-rule {
    position: absolute; left: 164px; right: 32px; top: 95px;
    height: 1px; background: var(--rule-grey);
  }
  .brand-tagline {
    position: absolute; left: 167px; top: 99px;
    font-size: 14.5px; font-weight: 500; color: var(--ink-dark);
  }
  .person-name {
    position: absolute; right: 33px; top: 64px;
    font-size: 23px; font-weight: 700; color: var(--ink-grey);
  }
  .person-title {
    position: absolute; right: 33px; top: 101px;
    font-size: 16px; color: var(--brand-green);
  }
  .edge-tab {
    position: absolute; right: 0; top: 68px;
    width: 9px; height: 47px; background: var(--brand-green);
  }

  /* front: contact list */
  .contact-list {
    position: absolute; left: 36px; top: 277px;
    list-style: none;
  }
  .contact-list li {
    display: flex; align-items: center;
    height: 19.5px;
    font-size: 16px; color: var(--ink-dark);
  }
  .contact-list svg {
    width: 13px; height: 13px; margin-right: 9px; fill: var(--ink-dark);
  }
  .address {
    position: absolute; right: 37px; top: 296px;
    text-align: right; font-size: 16px; line-height: 19.5px; color: var(--ink-dark);
  }
  .address .web {
    margin-top: 3px;
    color: var(--brand-green-deep); font-weight: 600;
  }

  /* back */
  .back-brand {
    position: absolute; left: 0; right: 0; top: 150px;
    display: flex; justify-content: center; align-items: center; gap: 18px;
  }
  .back-brand .dot {
    width: 44px; height: 44px; border-radius: 50%; background: var(--accent-yellow);
  }
  .back-brand .name {
    font-size: 52px; font-weight: 600; color: var(--reverse-text);
  }
  .back-web {
    position: absolute; left: 0; right: 0; top: 343px;
    text-align: center; font-size: 15.5px; letter-spacing: 2.4px;
    color: var(--reverse-text);
  }
</style>
</head>
<body>
  <section class="card card-front">
    <div class="brand-mark"></div>
    <div class="brand-name">BrambleWare</div>
    <div class="brand-rule"></div>
    <div class="brand-tagline">Student Success Platform</div>

    <div class="person-name">Daniel Harper</div>
    <div class="person-title">President</div>
    <div class="edge-tab"></div>

    <ul class="contact-list">
      <li><svg viewBox="0 0 16 16"><path d="M3.6 1.2l2.3 2.6-1.3 1.9c.9 2 2.6 3.7 4.6 4.6l1.9-1.3 2.6 2.3-1.4 2.3C7.400 14.800 1.200 8.600 1.300 2.600z"/></svg>555-214-7730</li>
      <li><svg viewBox="0 0 16 16"><path d="M4 0h8v16H4zM5.5 1.8v11h5v-11z"/></svg>555-618-2049</li>
      <li><svg viewBox="0 0 16 16"><path d="M4 1h7v4H4zM1 6h14v6H1zM3 10h10v5H3z"/></svg>555-903-4415</li>
      <li><svg viewBox="0 0 16 16"><path d="M1 3h14v10H1zM2.5 4.5L8 9l5.5-4.5z"/></svg>info@brambleware.com.au</li>
    </ul>

    <div class="address">
      <div>4120 Juniper Court</div>
      <div>Fairbanks, Alaska 99701</div>
      <div class="web">www.brambleware.com.au</div>
    </div>
  </section>

  <section class="card card-back">
    <div class="back-brand">
      <div class="dot"></div>
      <div class="name">BrambleWare</div>
    </div>
    <div class="back-web">www.brambleware.com.au</div>
  </section>
</body>
</html>
```